30th Anniversary Poster

Need a 2ft (Wide) X 3ft (Tall) Poster design for a 30th anniversary party that will be used in .  Need the get the logo to be the theme colors (gold).  Overall theme is elegance with gold and black being the main colors.  The background should be black.  Silver can be used as an accent color.  I need the sign to say Welcome and 30th Anniversary.  I need all text to be editable and fonts easily available.
A feel similar to images in this search is pretty close.
https://www.travinqo.example/find?sess=b7d2e90c41fa3318&ref=8K4QWTRB_plXM204XM204&tok=QPLMZNXdr4HwYbcEeRt2Uv:1650321478903&q=gala+event+poster&mode=4&flt=ZRPWk7Tt9pLmr41nQa8VcyXeHd2sBjKuvFgNoLQmRzT5Wp8xHcYbDe3KaNfVgUiJoPq7LrSt6MwXz2BvNcQhYdGeKjLmPoRsTuVwXyZaBcDeFgHiJkLmNoPqRsTuVwXyZaBcDeFgHiJkLmNoPqRsTuVw-3AbCdEfGhIj_KlMnOpQrStUvWxYzAbCdEfGhIjKlMnOpQrStUv-WxYzAbCdEfGhIj_KlMnOp&sb=Q&sk=4&vx=3bLPqRtw8Zn2KXwPmLrHnQsTUvWxYzAbCdEfGhIjKl&vw=1440&vh=900&px=2

```html
<!DOCTYPE html>
<html lang="en">
<head>
<meta charset="utf-8">
<title>30th Anniversary Party</title>
<link href="https://fonts.googleapis.com/css2?family=Great+Vibes&family=Montserrat:wght@600;700&family=Oswald:wght@700&display=swap" rel="stylesheet">
<style>
  :root {
    --black: #000000;
    --glow: #2b2729;
    --gold: #c9a24a;
    --gold-deep: #c28f2e;
    --gold-light: #fbf2c2;
    --gold-warm: #eba630;
    --white: #ffffff;
  }
  * { margin: 0; padding: 0; box-sizing: border-box; }
  html, body { width: 800px; height: 1200px; overflow: hidden; background: var(--black); }
  .poster {
    position: relative;
    width: 800px;
    height: 1200px;
    overflow: hidden;
    background: radial-gradient(ellipse 420px 420px at 400px 590px, var(--glow) 0%, #121012 55%, var(--black) 100%);
  }
  .decor { position: absolute; z-index: 1; }
  .frame-line { position: absolute; background: var(--gold); z-index: 3; }
  .frame-top-left { left: 60px; top: 109px; width: 214px; height: 1px; }
  .frame-top-right { left: 527px; top: 109px; width: 214px; height: 1px; }
  .frame-left { left: 60px; top: 109px; width: 1px; height: 984px; }
  .frame-right { left: 740px; top: 109px; width: 1px; height: 984px; }
  .frame-bottom { left: 60px; top: 1092px; width: 681px; height: 1px; }

  .brand-name {
    position: absolute;
    z-index: 2;
    left: 0; width: 800px; top: 84px;
    text-align: center;
    font-family: "Montserrat", sans-serif;
    font-weight: 600;
    font-size: 56px;
    line-height: 56px;
    letter-spacing: 1px;
    color: var(--white);
  }

  .welcome {
    position: absolute;
    z-index: 2;
    left: 0; width: 800px; top: 218px;
    text-align: center;
    font-family: "Montserrat", sans-serif;
    font-weight: 600;
    font-size: 22px;
    line-height: 28px;
    letter-spacing: 10px;
    padding-left: 10px;
    color: var(--gold);
  }

  .headline { position: absolute; z-index: 2; left: 0; top: 0; width: 800px; height: 900px; }
  .headline text { font-family: "Oswald", sans-serif; font-weight: 700; }
  .headline .label { font-family: "Montserrat", sans-serif; font-weight: 700; }

  .script-line {
    position: absolute;
    z-index: 2;
    left: 0; width: 800px; top: 700px;
    text-align: center;
    font-family: "Great Vibes", cursive;
    font-size: 112px;
    line-height: 130px;
    color: var(--white);
  }

  .confetti-top-left {
    left: 0; top: 0; width: 140px; height: 110px;
    background: radial-gradient(ellipse at 10% 20%, rgba(233,196,106,0.45), rgba(0,0,0,0) 70%);
  }
  .confetti-top-right {
    right: 0; top: 0; width: 140px; height: 80px;
    background: radial-gradient(ellipse at 90% 20%, rgba(233,196,106,0.45), rgba(0,0,0,0) 70%);
  }
  .streamer-top-left {
    left: 175px; top: 0; width: 115px; height: 120px;
    background: radial-gradient(ellipse at 50% 50%, rgba(214,170,80,0.45), rgba(0,0,0,0) 70%);
  }
  .streamer-top-right {
    left: 668px; top: 90px; width: 106px; height: 118px;
    background: radial-gradient(ellipse at 50% 50%, rgba(214,170,80,0.45), rgba(0,0,0,0) 70%);
  }
  .balloon-group {
    left: 0; top: 890px; width: 800px; height: 310px;
    background:
      radial-gradient(ellipse 80px 95px at 90px 90px, #f7db8a, rgba(0,0,0,0) 100%),
      radial-gradient(ellipse 72px 88px at 385px 135px, #f4e2aa, rgba(0,0,0,0) 100%),
      radial-gradient(ellipse 80px 95px at 605px 110px, #f6d67a, rgba(0,0,0,0) 100%),
      radial-gradient(ellipse 80px 90px at 170px 250px, #2a2a2c, rgba(0,0,0,0) 100%),
      radial-gradient(ellipse 75px 85px at 425px 260px, #2a2a2c, rgba(0,0,0,0) 100%),
      radial-gradient(ellipse 80px 90px at 700px 250px, #2a2a2c, rgba(0,0,0,0) 100%);
  }
</style>
</head>
<body>
<main class="poster">
  <div class="decor confetti-top-left" role="img" aria-label="Scattered gold star confetti"></div>
  <div class="decor confetti-top-right" role="img" aria-label="Scattered gold star confetti"></div>
  <div class="decor streamer-top-left" role="img" aria-label="Curled gold ribbon streamer"></div>
  <div class="decor streamer-top-right" role="img" aria-label="Curled gold ribbon streamer"></div>
  <div class="decor balloon-group" role="img" aria-label="Gold and black balloons with curled gold ribbons and star confetti"></div>

  <div class="frame-line frame-top-left"></div>
  <div class="frame-line frame-top-right"></div>
  <div class="frame-line frame-left"></div>
  <div class="frame-line frame-right"></div>
  <div class="frame-line frame-bottom"></div>

  <div class="brand-name">LOGO</div>
  <div class="welcome">WELCOME</div>

  <svg class="headline" viewBox="0 0 800 900" width="800" height="900">
    <defs>
      <linearGradient id="gold-sheen" x1="180" y1="330" x2="620" y2="600" gradientUnits="userSpaceOnUse">
        <stop offset="0" stop-color="#c28f2e"/>
        <stop offset="0.3" stop-color="#f3df9c"/>
        <stop offset="0.42" stop-color="#fbf2c2"/>
        <stop offset="0.55" stop-color="#eba630"/>
        <stop offset="0.68" stop-color="#c28f2e"/>
        <stop offset="0.85" stop-color="#f1d687"/>
        <stop offset="1" stop-color="#d59f36"/>
      </linearGradient>
      <linearGradient id="gold-label" x1="180" y1="0" x2="620" y2="0" gradientUnits="userSpaceOnUse">
        <stop offset="0" stop-color="#c9932f"/>
        <stop offset="0.45" stop-color="#f6e7a8"/>
        <stop offset="0.7" stop-color="#d9a23c"/>
        <stop offset="1" stop-color="#e9c36a"/>
      </linearGradient>
    </defs>
    <text x="199" y="604" font-size="352" textLength="288" lengthAdjust="spacingAndGlyphs" fill="url(#gold-sheen)">30</text>
    <text x="490" y="430" font-size="132" textLength="111" lengthAdjust="spacingAndGlyphs" fill="url(#gold-sheen)">TH</text>
    <text class="label" x="182" y="684" font-size="39" textLength="438" lengthAdjust="spacing" fill="url(#gold-label)">ANNIVERSARY</text>
  </svg>

  <div class="script-line">Party</div>
</main>
</body>
</html>
```